Company brochure for our unique consulting business

We are a small consulting business offering a unique set of services to our clients.. In simple terms we are a business improvement consultancy helping our clients get the best out of their businesses. We work with clients across multiple sectors and deliver a variety of services. We want to put together a brochure to cover these main themes:1. Who we are2. What we do3. The type of people we employ4. The sectors we work inWhile the brochure needs to have a certain corporate feel to it, we don't want it to be "boring" or "stiff". We would like it to have a slightly "friendly" or "informal" feel to it, to reflect the type of organisation we are.We have a company website http://tollandvergeadvisory.com , however we do not want to directly replicate the content or feel as we recognise it needs updating.We would like the brochure to be A4 portrait format. We anticipate requiring 12 sides (including covers) but we are happy to be guided on this based on the content we have provided.The attached ppt file gives the detail of the content to be included and also shows the proposed pagination. For the front cover we would like to try 2 versions, one with the TVA logo and one with the Tolland Verge Advisory logo (a file of both is attached)One of the most important pages will be the "Our Services" page. We would like this to cover the centre fold. In the ppt file we have shown an example layout, but this is where we need most help - we are clearly not graphic designers! This page will be the most used page in sales meetings etc.Also attached is the following:1. file for our TollandVerge Advisory company logo.2. File for our TVA company logo3. Files for Derek's signatures (for under photos) - Owen's to follow4. Photo of Derek & Owen (person in purple shirt to be cropped out)Thank you and really excited to see what everyone comes back with.Derek & Owen

Target Market(s)

Very broad - Manufacturing, Healthcare, Hospitality

Industry/Entity Type

Management Consulting

Font styles to use
Other font styles liked:
• We use Swiss721, but happy to be guided by designer

Colors
3276b5
85abd2
0355a3
333333
5c5c5c
9d9d9d
d9d9d9

Requirements
Must have
• Corporate feel
Nice to have
• Slightly friendly feel
• Our standard "blue" is (CORRECTION) - R55 G96 B146 #376092 and our standard grey is R197 G178, B179 - #B3B2B2, which we would like to keep, but other colours we are happy to be guided on. Brand guidelines attached.

```html
<!DOCTYPE html>
<html lang="en">
<head>
<meta charset="utf-8">
<title>Our Services – Tolland Verge Advisory</title>
<link href="https://fonts.googleapis.com/css2?family=Arimo:wght@400;700&display=swap" rel="stylesheet">
<style>
  :root {
    --blue-deep: #0355a3;
    --blue-brand: #376092;
    --blue-mid: #3276b5;
    --blue-light: #85abd2;
    --ink: #333333;
    --ink-soft: #5c5c5c;
    --grey: #9d9d9d;
    --rule: #d9d9d9;
    --paper: #ffffff;
    --backdrop: #e4e5e7;
  }
  * { box-sizing: border-box; margin: 0; padding: 0; }
  html, body { width: 1200px; height: 840px; overflow: hidden; }
  body {
    background: var(--backdrop);
    font-family: "Arimo", Arial, sans-serif;
    color: var(--ink);
    position: relative;
  }
  .spread {
    position: absolute;
    left: 60px; top: 38px;
    width: 1080px; height: 764px;
    display: flex;
    box-shadow: 0 6px 24px rgba(0,0,0,0.12);
  }
  .page {
    position: relative;
    width: 540px; height: 764px;
    background: var(--paper);
  }
  .page--left { background: linear-gradient(to right, #fff 88%, #eef0f3 100%); }
  .page--right { background: linear-gradient(to left, #fff 88%, #eef0f3 100%); }

  .services-heading {
    position: absolute;
    left: 56px; top: 74px;
    display: flex;
    align-items: stretch;
    font-size: 22px;
    font-weight: 700;
    letter-spacing: 0.5px;
    border-bottom: 2px solid var(--blue-deep);
  }
  .services-heading__our {
    color: var(--blue-deep);
    border: 2px solid var(--blue-deep);
    border-bottom: none;
    padding: 2px 6px 0;
  }
  .services-heading__main {
    background: var(--blue-deep);
    color: #fff;
    padding: 4px 10px 2px;
  }
  .services-intro {
    position: absolute;
    left: 56px; top: 116px;
    width: 430px;
    font-size: 8.5px;
    line-height: 1.5;
    color: var(--ink-soft);
  }
  .brand-name {
    position: absolute;
    left: 40px; bottom: 18px;
    font-size: 14px;
    font-weight: 700;
    color: var(--blue-brand);
    letter-spacing: 0.5px;
  }
  .page-number {
    position: absolute;
    right: 30px; bottom: 18px;
    font-size: 11px;
    color: var(--ink-soft);
  }
  .services-map {
    position: absolute;
    left: 0; top: 0;
    width: 1080px; height: 764px;
    pointer-events: none;
  }
  .node { fill: #fff; stroke: var(--blue-light); stroke-width: 1; }
  .node-label { font-size: 6.3px; fill: var(--ink-soft); text-anchor: middle; }
  .link { stroke: var(--blue-light); stroke-width: 0.8; }
  .link--main { stroke: var(--blue-mid); stroke-width: 1.2; }
  .hub { fill: var(--blue-deep); stroke: var(--blue-light); stroke-width: 3; }
  .hub-title { font-size: 13px; font-weight: 700; fill: #fff; text-anchor: middle; }
  .hub-sub { font-size: 6.3px; fill: #cfe0f2; text-anchor: middle; }
  .core { fill: var(--blue-deep); stroke: #fff; stroke-width: 2; }
  .core-label { font-size: 8.5px; font-weight: 700; fill: #fff; text-anchor: middle; }
  .band { fill: var(--blue-deep); }
  .footer-rule { stroke: var(--blue-mid); stroke-width: 0.8; }
</style>
</head>
<body>
<div class="spread">
  <section class="page page--left">
    <h1 class="services-heading"><span class="services-heading__our">OUR</span><span class="services-heading__main">SERVICES</span></h1>
    <p class="services-intro">We recognise every organisation we work with is different; the products or services provided, the outlook and the readiness for change but most importantly the people and the culture. We combine the skills, knowledge and experience across our team meaning we are able to offer an extensive range of services which are tailored to meet your specific needs.</p>
    <div class="brand-name">TVA</div>
  </section>
  <section class="page page--right">
    <div class="page-number">7</div>
  </section>

  <svg class="services-map" viewBox="0 0 1080 764" aria-label="Services map">
    <defs>
      <polygon id="hex-sm" points="-24,0 -12,-20.8 12,-20.8 24,0 12,20.8 -12,20.8"/>
      <polygon id="hex-lg" points="-62,0 -31,-53.7 31,-53.7 62,0 31,53.7 -31,53.7"/>
      <polygon id="hex-core" points="-34,0 -17,-29.4 17,-29.4 34,0 17,29.4 -17,29.4"/>
    </defs>

    <polygon class="band" points="230,20 540,20 540,31"/>
    <polygon class="band" points="540,20 1080,20 1080,34 700,24"/>
    <line class="footer-rule" x1="90" y1="740" x2="540" y2="740"/>
    <line class="footer-rule" x1="540" y1="740" x2="1020" y2="740"/>

    <line class="link link--main" x1="250" y1="420" x2="540" y2="480"/>
    <line class="link link--main" x1="540" y1="480" x2="820" y2="320"/>
    <line class="link link--main" x1="540" y1="480" x2="760" y2="590"/>

    <!-- Business Improvement -->
    <g class="cluster cluster--business">
      <g class="link">
        <line x1="250" y1="420" x2="250" y2="265"/><line x1="250" y1="420" x2="317" y2="280"/>
        <line x1="250" y1="420" x2="371" y2="323"/><line x1="250" y1="420" x2="401" y2="386"/>
        <line x1="250" y1="420" x2="401" y2="454"/><line x1="250" y1="420" x2="371" y2="517"/>
        <line x1="250" y1="420" x2="317" y2="560"/><line x1="250" y1="420" x2="250" y2="575"/>
        <line x1="250" y1="420" x2="183" y2="560"/><line x1="250" y1="420" x2="129" y2="517"/>
        <line x1="250" y1="420" x2="99" y2="454"/><line x1="250" y1="420" x2="99" y2="386"/>
        <line x1="250" y1="420" x2="129" y2="323"/><line x1="250" y1="420" x2="183" y2="280"/>
      </g>
      <g transform="translate(250,265)"><use href="#hex-sm" class="node"/><text class="node-label"><tspan x="0" y="-1">Operational</tspan><tspan x="0" y="7">Design</tspan></text></g>
      <g transform="translate(317,280)"><use href="#hex-sm" class="node"/><text class="node-label"><tspan x="0" y="-1">Strategic</tspan><tspan x="0" y="7">Planning</tspan></text></g>
      <g transform="translate(371,323)"><use href="#hex-sm" class="node"/><text class="node-label"><tspan x="0" y="-1">Training</tspan><tspan x="0" y="7">Needs</tspan></text></g>
      <g transform="translate(401,386)"><use href="#hex-sm" class="node"/><text class="node-label"><tspan x="0" y="-1">Lean</tspan><tspan x="0" y="7">Review</tspan></text></g>
      <g transform="translate(401,454)"><use href="#hex-sm" class="node"/><text class="node-label"><tspan x="0" y="-1">Cost</tspan><tspan x="0" y="7">Reduction</tspan></text></g>
      <g transform="translate(371,517)"><use href="#hex-sm" class="node"/><text class="node-label"><tspan x="0" y="-1">Change</tspan><tspan x="0" y="7">Management</tspan></text></g>
      <g transform="translate(317,560)"><use href="#hex-sm" class="node"/><text class="node-label"><tspan x="0" y="-1">Capacity</tspan><tspan x="0" y="7">Planning</tspan></text></g>
      <g transform="translate(250,575)"><use href="#hex-sm" class="node"/><text class="node-label"><tspan x="0" y="-1">Team</tspan><tspan x="0" y="7">Development</tspan></text></g>
      <g transform="translate(183,560)"><use href="#hex-sm" class="node"/><text class="node-label"><tspan x="0" y="-1">Performance</tspan><tspan x="0" y="7">Reporting</tspan></text></g>
      <g transform="translate(129,517)"><use href="#hex-sm" class="node"/><text class="node-label"><tspan x="0" y="-1">Supply</tspan><tspan x="0" y="7">Chain</tspan></text></g>
      <g transform="translate(99,454)"><use href="#hex-sm" class="node"/><text class="node-label"><tspan x="0" y="-1">Supplier</tspan><tspan x="0" y="7">Review</tspan></text></g>
      <g transform="translate(99,386)"><use href="#hex-sm" class="node"/><text class="node-label"><tspan x="0" y="-1">Process</tspan><tspan x="0" y="7">Mapping</tspan></text></g>
      <g transform="translate(129,323)"><use href="#hex-sm" class="node"/><text class="node-label"><tspan x="0" y="-1">Quality</tspan><tspan x="0" y="7">Systems</tspan></text></g>
      <g transform="translate(183,280)"><use href="#hex-sm" class="node"/><text class="node-label"><tspan x="0" y="-1">Business</tspan><tspan x="0" y="7">Assessment</tspan></text></g>
      <g transform="translate(250,420)">
        <use href="#hex-lg" class="hub"/>
        <text class="hub-title"><tspan x="0" y="-10">Business</tspan><tspan x="0" y="5">Improvement</tspan></text>
        <text class="hub-sub"><tspan x="0" y="18">Helping your organisation</tspan><tspan x="0" y="26">perform at its best</tspan></text>
      </g>
    </g>

    <!-- Organisational Readiness -->
    <g class="cluster cluster--readiness">
      <g class="link">
        <line x1="820" y1="320" x2="707" y2="279"/><line x1="820" y1="320" x2="760" y2="216"/>
        <line x1="820" y1="320" x2="841" y2="202"/><line x1="820" y1="320" x2="912" y2="243"/>
        <line x1="820" y1="320" x2="940" y2="320"/><line x1="820" y1="320" x2="912" y2="397"/>
      </g>
      <g transform="translate(707,279)"><use href="#hex-sm" class="node"/><text class="node-label" y="3">Sale</text></g>
      <g transform="translate(760,216)"><use href="#hex-sm" class="node"/><text class="node-label" y="3">Acquisitions</text></g>
      <g transform="translate(841,202)"><use href="#hex-sm" class="node"/><text class="node-label" y="3">Divestment</text></g>
      <g transform="translate(912,243)"><use href="#hex-sm" class="node"/><text class="node-label" y="3">Merger</text></g>
      <g transform="translate(940,320)"><use href="#hex-sm" class="node"/><text class="node-label" y="3">Growth</text></g>
      <g transform="translate(912,397)"><use href="#hex-sm" class="node"/><text class="node-label" y="3">Optimisation</text></g>
      <g transform="translate(820,320)">
        <use href="#hex-lg" class="hub"/>
        <text class="hub-title"><tspan x="0" y="-10">Organisational</tspan><tspan x="0" y="5">Readiness</tspan></text>
        <text class="hub-sub"><tspan x="0" y="18">Making sure your business</tspan><tspan x="0" y="26">is ready for a future</tspan></text>
      </g>
    </g>

    <!-- Programme Management -->
    <g class="cluster cluster--programme">
      <g class="link">
        <line x1="760" y1="590" x2="705" y2="495"/><line x1="760" y1="590" x2="770" y2="480"/>
        <line x1="760" y1="590" x2="831" y2="506"/><line x1="760" y1="590" x2="866" y2="562"/>
        <line x1="760" y1="590" x2="863" y2="628"/><line x1="760" y1="590" x2="823" y2="680"/>
        <line x1="760" y1="590" x2="760" y2="700"/><line x1="760" y1="590" x2="697" y2="680"/>
        <line x1="760" y1="590" x2="657" y2="628"/>
      </g>
      <g transform="translate(705,495)"><use href="#hex-sm" class="node"/><text class="node-label"><tspan x="0" y="-1">Quality</tspan><tspan x="0" y="7">Assurance</tspan></text></g>
      <g transform="translate(770,480)"><use href="#hex-sm" class="node"/><text class="node-label"><tspan x="0" y="-1">Risk</tspan><tspan x="0" y="7">Management</tspan></text></g>
      <g transform="translate(831,506)"><use href="#hex-sm" class="node"/><text class="node-label"><tspan x="0" y="-1">Project</tspan><tspan x="0" y="7">Planning</tspan></text></g>
      <g transform="translate(866,562)"><use href="#hex-sm" class="node"/><text class="node-label"><tspan x="0" y="-1">Vendor</tspan><tspan x="0" y="7">Selection</tspan></text></g>
      <g transform="translate(863,628)"><use href="#hex-sm" class="node"/><text class="node-label" y="3">PMO</text></g>
      <g transform="translate(823,680)"><use href="#hex-sm" class="node"/><text class="node-label"><tspan x="0" y="-1">Cost</tspan><tspan x="0" y="7">Control</tspan></text></g>
      <g transform="translate(760,700)"><use href="#hex-sm" class="node"/><text class="node-label"><tspan x="0" y="-1">Customer</tspan><tspan x="0" y="7">Acceptance</tspan></text></g>
      <g transform="translate(697,680)"><use href="#hex-sm" class="node"/><text class="node-label"><tspan x="0" y="-1">IT Systems</tspan><tspan x="0" y="7">Rollout</tspan></text></g>
      <g transform="translate(657,628)"><use href="#hex-sm" class="node"/><text class="node-label"><tspan x="0" y="-1">Resource</tspan><tspan x="0" y="7">Planning</tspan></text></g>
      <g transform="translate(760,590)">
        <use href="#hex-lg" class="hub"/>
        <text class="hub-title"><tspan x="0" y="-10">Programme</tspan><tspan x="0" y="5">Management</tspan></text>
        <text class="hub-sub"><tspan x="0" y="18">Managing your projects</tspan><tspan x="0" y="26">through to delivery</tspan></text>
      </g>
    </g>

    <g transform="translate(540,480)">
      <use href="#hex-core" class="core"/>
      <text class="core-label"><tspan x="0" y="-2">OUR</tspan><tspan x="0" y="9">SERVICES</tspan></text>
    </g>
  </svg>
</div>
</body>
</html>
```